Tarrowind High School Association Website New Design

We require a fresh new website design for the Tarrowind High School Old Boys Association. The association is a non-for-profit and as such we like the site to reflect the ethos.
We require a design that uses responsive design techniques, so to allow the site to shift between mobile, tablet and desktop spaces and maintain elements in the site.
We would like a landing/home page design, and also an inner news/article based design included.
We want the site to appeal to a broad market of both the old guard members but also to bring on board the new social savey younger members.
The site needs to have a modern take on a professional yet fresh and opulent/elegant look.
A site that we like influences from is http://www.quennaval-lodge.com/ we especially like the navigation look and feel.
The site needs to be clean and simple to find information and navigate and as such would like the site design elements to reflect this in its layout and element interplay.
This site will act as an information gateway for the member's, but also offer abilities to purchase memberships, get information on up coming events and purchase tickets to these events, and interact with the members on the site.
Hi All designers,
The client has now agreed to make the project funding guaranteed, so I hope to see some great designs from you.
Thanks
Sorry all, I hadn't uploaded the logo, has now been uploaded.
Hi all designers, please don't let the wireframe layout include restrict your design freedom on the page layout. We included this to give you a feel for the elements wanted in the site, but not to push you to have them all in that arrangement. Feel free to move around or remove parts of to make better use of the space.
Also this site is for ex-students who are members of an association linked to the school, and not for the school itself, so your designs need to lean towards a member, events and reunions type site design.
After a review today, client now requires that the sites Events need special consideration. Want to see in a prominent position on the landing page area a good area to showcase the upcoming events. Please take this into consideration in your future design layouts.
Hi All Designers, I appreciate all the new and current designs, and sorry a bit behind on the feedback, have been a bit swamped on my own workload, I will give feedback to you all, and will maybe look at an extension of the deadline if need be, as to also allow the clients to look over designs.
Thanks
Reason: Extending the project deadline to allow more feedback to be provider to all designers, to allow review by clients and the feedback through myself.
Reason: Client was un-available for comment, and want them to be able to give feedback to designers for last round updates.
Reason: Sorry all, client has been overseas, and will only be back next week, so need to extend the deadline to allow for client input next week.
Reason: Sorry client has be delayed overseas, so when be needing to work through the designs next week to allow full ability to give all designs due recognition.
Reason: Waiting for client to review designs.
Target Market(s)
Professionals from all varity of job types
Industry/Entity Type
Events
Requirements
Must have
- Please use the attached Logo in the design and look to use the current colour pallet as much as possible, but open to colour and pallet additions or amendments.
Must have a “hero” header image scroller for ability to showcase upcoming events and other items (Required for home/landing pages, could be amended or removed on inner pages).
Should look to follow the include wire frame layout concept as a good conception starting point - but do not limit to just this layout, use design discretion.
Include prominently positioned events area in layout for upcoming events to push the events heavy aspect of the site.
Should include icons/link abilities to access social sites and applications. Ie Plumvine etc.
Nice to have
- A modern look with an edge to it.
Creative use of the sites colour pallet and site elements.
Should not have
- should not be a copy of the wireframe with colour added

```html
<!DOCTYPE html>
<html lang="en">
<head>
<meta charset="utf-8">
<title>Tarrowind High School Old Boys Association</title>
<link href="https://fonts.googleapis.com/css2?family=Arimo:wght@400;700&display=swap" rel="stylesheet">
<style>
:root{
  --green-deep:#0c3f24;
  --green-dark:#145a32;
  --green-mid:#2a7a3f;
  --green-page1:#3f8a4e;
  --green-page2:#1b5c33;
  --orange:#e2711d;
  --red:#c5342b;
  --paper:#ffffff;
  --panel:#eeeeea;
  --line:#d5d7cf;
  --ink:#333333;
  --muted:#777777;
}
*{box-sizing:border-box;margin:0;padding:0}
html,body{width:900px;height:1200px;overflow:hidden}
body{font-family:"Arimo",Arial,sans-serif;color:var(--ink);
  background:linear-gradient(180deg,var(--green-page2) 0,var(--green-page1) 300px,var(--green-mid) 700px,var(--green-page2) 1060px);position:relative}
.site-header{position:absolute;left:0;top:0;width:900px;height:76px;background:var(--green-deep)}
.brand{position:absolute;left:111px;top:20px;display:flex;align-items:center;gap:10px}
.brand-square{width:14px;height:14px;background:var(--paper)}
.brand-name{color:#fff;font-weight:700;font-size:22px}
.brand-title{color:#fff;font-size:14px;font-weight:700;margin-left:10px}
.search{position:absolute;left:660px;top:30px;display:flex}
.search-field{width:96px;height:18px;background:#e6ebe4;border:1px solid #9fb7a2}
.search-btn{height:18px;padding:0 8px;background:var(--orange);color:#fff;font-size:9px;font-weight:700;line-height:18px}
.main-nav{position:absolute;left:105px;top:80px;width:690px;height:24px;background:linear-gradient(#f2f2ee,#c9cdc3);display:flex;border:1px solid #a9b3a5}
.main-nav a{flex:1;text-align:center;font-size:10px;font-weight:700;color:var(--green-dark);text-decoration:none;line-height:22px;border-right:1px solid #aeb6aa}
.main-nav a:last-child{border-right:0}
.hero{position:absolute;left:105px;top:106px;width:690px;height:296px;border:3px solid #fff;
  background:linear-gradient(160deg,#8fb08a 0,#4d6b52 35%,#2c2a25 65%,#6b5a42 100%)}
.hero-dots{position:absolute;left:12px;bottom:10px;display:flex;gap:5px}
.hero-dots span{width:7px;height:7px;border-radius:50%;background:#fff;opacity:.5}
.hero-dots span:first-child{opacity:1}
.content{position:absolute;left:105px;top:414px;width:690px;height:640px;background:var(--paper)}
.events-side{position:absolute;left:6px;top:6px;width:207px;height:628px;background:var(--panel);padding:10px 10px}
.side-kicker{font-size:9px;font-weight:700;color:var(--muted);letter-spacing:.5px}
.side-title{font-size:20px;font-weight:700;color:var(--red);border-bottom:2px solid var(--green-mid);padding-bottom:4px;margin-bottom:8px}
.side-event{border-bottom:1px dotted #b9bdb2;padding:6px 0}
.side-event h3{font-size:11px;color:var(--green-dark)}
.side-event .date{font-size:9px;color:var(--red);margin:1px 0 4px}
.side-event .row{display:flex;gap:6px;font-size:8.5px;line-height:1.3;color:#555}
.thumb{flex:none;width:58px;height:44px;background:linear-gradient(135deg,#7d9a78,#3b5a40)}
.link{color:var(--green-mid);font-weight:700;font-size:9px;text-decoration:underline}
.feature{position:absolute;left:231px;top:6px;width:453px}
.feature-title{background:var(--green-dark);color:#fff;font-size:15px;font-weight:700;padding:5px 8px}
.feature-date{font-size:9px;color:var(--muted);margin:4px 8px}
.feature-body{display:flex;gap:12px;padding:6px 8px}
.feature-img{flex:none;width:150px;height:100px;border:3px solid #ddd;background:linear-gradient(135deg,#c9a46a,#6d3f22 60%,#e8e2d5)}
.feature-text p{font-size:9.5px;line-height:1.45;color:#555;margin-bottom:6px}
.week-head{position:absolute;left:231px;top:186px;width:453px;display:flex;justify-content:space-between;align-items:center;border-bottom:2px solid var(--green-mid);padding:0 4px 4px}
.week-head h2{font-size:15px;color:var(--green-dark)}
.week-head .sub{font-size:9px;color:var(--muted);font-weight:400;display:block}
.arrows{display:flex;gap:3px}
.arrows svg{width:16px;height:16px}
.calendar{position:absolute;left:231px;top:226px;width:453px;border-collapse:collapse;font-size:9px}
.calendar th{background:var(--green-deep);color:#fff;height:20px;font-weight:700}
.calendar td{height:26px;border:1px solid var(--line);text-align:right;vertical-align:top;padding:3px 5px;background:#f4f5f1}
.calendar td.today{background:var(--green-dark);color:#fff}
.calendar td.empty{background:#e4e6df}
.week-list{position:absolute;left:231px;top:390px;width:453px}
.week-item{display:flex;gap:10px;border-bottom:1px dotted #b9bdb2;padding:8px 4px}
.day{flex:none;width:80px;background:var(--panel);padding:6px}
.day b{display:block;font-size:11px;color:var(--green-dark)}
.day span{font-size:8.5px;color:var(--red)}
.week-item p{font-size:9.5px;line-height:1.45;color:#555}
.site-footer{position:absolute;left:0;top:1062px;width:900px;height:138px;background:var(--green-deep);color:#d9e6da;display:flex;padding:14px 105px;gap:30px}
.foot-col{flex:1}
.foot-col h4{font-size:10px;color:var(--red);font-weight:700;margin-bottom:7px;letter-spacing:.3px}
.foot-col li{list-style:none;font-size:9px;line-height:1.7}
.foot-col li::before{content:"\25B8  ";color:var(--orange)}
.contact li::before{content:""}
.social{display:flex;gap:6px;margin-bottom:10px}
.social span{width:44px;height:24px;background:var(--green-mid);color:#fff;font-size:8px;line-height:24px;text-align:center}
.newsletter{display:flex}
.newsletter .field{width:110px;height:18px;background:#e6ebe4}
.newsletter .join{background:var(--red);color:#fff;font-size:9px;font-weight:700;padding:0 10px;line-height:18px}
</style>
</head>
<body>
<header class="site-header">
  <div class="brand"><span class="brand-square"></span><span class="brand-name">Tarrowind</span><span class="brand-title">Tarrowind High School Old Boys Association</span></div>
  <div class="search"><span class="search-field"></span><span class="search-btn">SEARCH</span></div>
</header>
<nav class="main-nav"><a>HOME</a><a>NEWS</a><a>EVENTS</a><a>PHOTOS</a><a>MEMBERSHIP</a><a>CONTACT</a></nav>
<div class="hero" role="img" aria-label="Photo of a school band performing in a large hall">
  <div class="hero-dots"><span></span><span></span><span></span><span></span><span></span></div>
</div>

<main class="content">
  <aside class="events-side">
    <div class="side-kicker">UPCOMING</div>
    <div class="side-title">EVENTS !!</div>
    <div class="side-event"><h3>New Golf Day: The Alder Trophy</h3><div class="date">Wednesday 14 September 2012</div>
      <div class="row"><span class="thumb" role="img" aria-label="Golf course photo"></span><span>Due to great demand we are pleased to announce the TOBA Alder Trophy Golf Day on Monday 24 September. <b class="link">More</b></span></div></div>
    <div class="side-event"><h3>Harlow Bay Luncheon: Mr Owen Halbrook</h3><div class="date">Wednesday 14 September 2012</div>
      <div class="row"><span class="thumb" role="img" aria-label="Luncheon guest photo"></span><span>The 5th of our Harlow Bay luncheons at the Harlow Bay Club on Kestrel Street will be held at 12.00pm. <b class="link">More</b></span></div></div>
    <div class="side-event"><h3>TOBA Winemaker Series</h3><div class="date">Tuesday 23 August 2012</div>
      <div class="row"><span class="link">Online bookings</span></div></div>
    <div class="side-event"><h3>TOBA Soccer game</h3><div class="date">Tuesday 23 August 2012</div>
      <div class="row"><span class="thumb" role="img" aria-label="Soccer ball photo"></span><span>Football game being hosted on 16 September 2012 at 11.00pm for 1.00pm start. <b class="link">More</b></span></div></div>
  </aside>

  <section class="feature">
    <h2 class="feature-title">TOBA Winemaker Dinner Series</h2>
    <div class="feature-date">Wednesday 15 August 2012</div>
    <div class="feature-body">
      <div class="feature-img" role="img" aria-label="Plated dinner with steak and vegetables"></div>
      <div class="feature-text">
        <p>The TOBA Constitution outlines the operational structure of our Old Boys' Club. It is reprinted each year as an attachment to the AGM and dinner booklet.</p>
        <p>Your TOBA Board outlines the operational structure of our Club. It is reprinted each year as an attachment to the AGM and dinner booklet.</p>
        <span class="link">Online bookings</span>
      </div>
    </div>
  </section>

  <div class="week-head">
    <h2>NEXT WEEK AT CORRIN HOTEL<span class="sub">Wednesday 15 August 2012</span></h2>
    <div class="arrows">
      <svg viewBox="0 0 16 16"><circle cx="8" cy="8" r="8" fill="#2a7a3f"/><path d="M10 4L6 8l4 4" stroke="#fff" stroke-width="2" fill="none"/></svg>
      <svg viewBox="0 0 16 16"><circle cx="8" cy="8" r="8" fill="#2a7a3f"/><path d="M6 4l4 4-4 4" stroke="#fff" stroke-width="2" fill="none"/></svg>
    </div>
  </div>
  <table class="calendar">
    <tr><th>Sun</th><th>Mon</th><th>Tue</th><th>Wed</th><th>Thu</th><th>Fri</th><th>Sat</th></tr>
    <tr><td class="empty"></td><td class="empty"></td><td class="empty"></td><td>1</td><td>2</td><td>3</td><td>4</td></tr>
    <tr><td>5</td><td>6</td><td>7</td><td>8</td><td>9</td><td>10</td><td>11</td></tr>
    <tr><td>12</td><td>13</td><td>14</td><td class="today">15</td><td>16</td><td>17</td><td>18</td></tr>
    <tr><td>19</td><td>20</td><td>21</td><td>22</td><td>23</td><td>24</td><td>25</td></tr>
    <tr><td>26</td><td>27</td><td>28</td><td>29</td><td>30</td><td>31</td><td class="empty"></td></tr>
  </table>
  <div class="week-list">
    <div class="week-item"><div class="day"><b>Saturday</b><span>18 August</span></div>
      <p>The TOBA Constitution outlines the operational structure of our Old Boys' Club. It is reprinted each year as an attachment to the AGM and dinner booklet. <b class="link">More</b></p></div>
    <div class="week-item"><div class="day"><b>Sunday</b><span>19 August</span></div>
      <p>The TOBA Constitution outlines the operational structure of our Old Boys' Club, reprinted each year for the AGM and dinner booklet. <b class="link">More</b></p></div>
  </div>
</main>

<footer class="site-footer">
  <div class="foot-col"><h4>HEADING TO GO HERE</h4>
    <ul><li>payment</li><li>about us</li><li>contact us</li><li>links</li></ul></div>
  <div class="foot-col contact"><h4>CONTACT US</h4>
    <ul><li>P | (03) 5550 1842</li><li>E | info@toba-club.org</li><li>W | www.toba-club.org</li><li>A | 12 Kestrel Street, Tarrowind</li></ul></div>
  <div class="foot-col"><h4>GET SOCIAL</h4>
    <div class="social"><span>Plumvine</span><span>Feed</span><span>Chirper</span></div>
    <h4>NEWSLETTER</h4>
    <div class="newsletter"><span class="field"></span><span class="join">Join</span></div></div>
</footer>
</body>
</html>
```